Fresh and unique Mortgage Broking business needs website design.

We need a professional yet fresh, bright and colourful website for my Mortgage broking business.
We specialise in the Non conforming/sub prime market with clients who have been rejected by other banks or have trouble getting finance through a traditional lender.
We are called Brightwell Lending and we aim to provide Hope to our clients when they have thought there was no hope.
I would like it to be on a Wordpress platform as I plan to do a lot of postings, both written and video and I need it to be easy to use.
I would also like it to be able to have a clear and simple enquiry box on the first page to capture contact details and notify me via email.

I have already had the logo designed in both green and black and a white version.
I have also had a a header made up using the white logo with leaves background that could possibly be used as the website header which I have used as my facebook header.

https://www.facebook.com/MarcusTolvenBright/

I tried playing around with a jimdo website builder which kind of got some of the brightness and colours I was after but it had a lot to go.

http://brightwelllending.sitevale.example/

Industry/Entity Type

Finance

Number of Pages Required

4 page

Colors
0292cd
00a990
fbed22
ffc214
f78f20
ec1f27

Requirements
Nice to have
• I'm not sure what the difference between uncoded and coded website is so I'm not sure what I need?

```html
<!DOCTYPE html>
<html lang="en">
<head>
<meta charset="utf-8">
<title>Brightwell Lending — Mortgage Broking</title>
<link rel="stylesheet" href="https://fonts.googleapis.com/css2?family=Lato:wght@400;700;900&family=Merriweather:wght@700&display=swap">
<style>
:root{
  --blue:#0292cd;--teal:#00a990;--lemon:#fbed22;--yellow:#ffc214;--orange:#f78f20;--red:#ec1f27;
  --ink:#333;--muted:#8a8a8a;--line:#e3e3e3;--soft:#f4f4f4;--dark:#2f2f2f;--darker:#1f1f1f;--white:#fff;
}
*{margin:0;padding:0;box-sizing:border-box}
html,body{width:1200px;height:3380px;overflow:hidden}
body{font-family:"Lato",sans-serif;color:var(--ink);background:var(--white);font-size:15px}
.serif{font-family:"Merriweather",serif}
section,header,footer{position:relative;width:1200px}

/* hero */
.hero{height:608px;overflow:hidden}
.hero-photo{position:absolute;inset:0;background:linear-gradient(120deg,#6f8460 0%,#a7a48a 35%,#7d6b58 60%,#4c5a43 100%)}
.hero-shade{position:absolute;inset:0;background:rgba(0,0,0,.25)}
.topbar{position:absolute;top:0;left:0;right:0;height:40px;display:flex;justify-content:space-between;align-items:center;padding:0 130px;color:var(--white);font-size:13px}
.topbar .phone{display:flex;align-items:center;gap:8px}
.social{display:flex;gap:10px}
.social span{width:22px;height:22px;border-radius:50%;display:block}
.brand{position:absolute;top:22px;left:0;right:0;text-align:center;color:var(--white);font-weight:900;font-size:26px;display:flex;justify-content:center;align-items:center;gap:10px}
.brand i{width:14px;height:14px;border-radius:50%;background:var(--white);display:block}
.nav{position:absolute;top:124px;left:0;right:0;display:flex;justify-content:center;gap:40px;font-size:14px;color:var(--white)}
.nav a{color:inherit;text-decoration:none;padding:6px 12px}
.nav a.active{background:var(--yellow);color:var(--dark);border-radius:2px}
.hero-copy{position:absolute;top:300px;left:0;right:0;text-align:center;color:var(--white)}
.hero-copy h1{font-size:46px;color:var(--yellow);letter-spacing:1px}
.hero-copy p{width:620px;margin:18px auto 0;font-size:17px;line-height:1.6}
.btn-ghost{display:inline-block;margin-top:44px;border:2px solid var(--yellow);border-radius:20px;padding:10px 32px;font-size:12px;font-weight:700;color:var(--white);letter-spacing:1px}
.arrow{position:absolute;top:320px;width:24px;height:24px}
.arrow.l{left:130px}.arrow.r{right:130px}

/* rates */
.rates{height:692px;background:var(--soft)}
.sec-title{text-align:center;color:var(--teal);font-size:30px;padding-top:110px}
.sec-sub{text-align:center;color:var(--muted);font-size:14px;line-height:1.6;width:560px;margin:14px auto 0}
.cards{position:absolute;top:264px;left:152px;display:flex;gap:24px}
.card{width:206px;height:330px;background:var(--white);border:1px solid var(--line);text-align:center}
.card h3{color:var(--white);font-size:15px;padding:14px 0;font-weight:700}
.card .rate{font-size:34px;font-weight:400;margin-top:24px}
.card small{display:block;font-size:10px;color:var(--muted);letter-spacing:1px;margin-top:4px}
.card hr{border:0;border-top:1px solid var(--line);margin:20px 24px 0}
.btn{display:inline-block;background:var(--blue);color:var(--white);font-size:12px;font-weight:700;padding:10px 26px;border-radius:20px;margin-top:22px}
.c1 h3{background:var(--orange)}.c2 h3{background:var(--yellow)}.c3 h3{background:var(--teal)}.c4 h3{background:var(--red)}

/* feature band */
.feature{height:480px;display:flex}
.feature-photo{width:600px;height:480px;background:linear-gradient(135deg,#8c7e6a,#c3a36a 55%,#6e6a5e)}
.feature-copy{width:600px;height:480px;background:var(--yellow);padding:80px 60px 0 30px;color:var(--white)}
.feature-copy h2{font-size:34px}
.feature-copy .lead{font-size:21px;line-height:1.4;margin-top:18px}
.feature-copy p{font-size:13px;line-height:1.7;margin-top:20px;color:#5a4a12}
.feature-copy .btn-ghost{margin-top:24px;border-color:var(--white);color:var(--white)}

/* about */
.about{height:440px}
.about h2{position:absolute;left:152px;top:88px;font-size:44px;color:var(--blue);font-weight:700}
.about .intro{position:absolute;left:152px;top:162px;width:420px;font-size:20px;line-height:1.4;color:var(--muted)}
.about .body{position:absolute;left:152px;top:270px;width:420px;font-size:13px;line-height:1.7;color:var(--muted)}
.about-photo1{position:absolute;left:660px;top:60px;width:250px;height:230px;background:linear-gradient(135deg,#e9d9c2,#b79670)}
.about-photo2{position:absolute;left:780px;top:130px;width:240px;height:260px;background:linear-gradient(160deg,#c9c9c9,#4c4c4c);border:6px solid var(--white);box-shadow:0 2px 10px rgba(0,0,0,.2)}

/* testimonials */
.testimonials{height:572px;background:var(--soft)}
.testimonials .sec-title{padding-top:56px;color:var(--teal);font-size:34px}
.tcards{position:absolute;top:180px;left:152px;display:flex;gap:12px}
.tcard{width:292px;height:364px;background:var(--white);border:1px solid var(--line);text-align:center}
.tphoto{height:200px}
.tcard h4{color:var(--teal);font-size:17px;margin-top:22px}
.tcard p{font-size:12px;line-height:1.6;color:var(--muted);padding:12px 24px 0}

/* consultation */
.consult{height:316px;overflow:hidden}
.consult-photo{position:absolute;inset:0;background:linear-gradient(120deg,#5f5a52,#8e8678 50%,#5a544a)}
.consult-shade{position:absolute;inset:0;background:rgba(0,0,0,.35)}
.consult h2{position:relative;text-align:center;color:var(--white);font-size:40px;padding-top:56px}
.form{position:absolute;top:168px;left:152px;display:flex;gap:20px}
.field{width:280px;height:38px;border:1px solid rgba(255,255,255,.6);background:rgba(255,255,255,.12);color:var(--white);font-size:12px;padding:11px 14px}
.submit{position:absolute;top:240px;left:0;right:0;text-align:center}
.submit span{display:inline-block;background:var(--yellow);color:var(--dark);font-weight:700;font-size:13px;padding:11px 40px;border-radius:20px}

/* footer */
.footer{height:220px;background:var(--dark);color:#bdbdbd;display:flex;gap:0;padding:40px 0 0 152px}
.fcol{width:300px;font-size:12px;line-height:2}
.fcol h5{color:var(--yellow);font-size:14px;margin-bottom:8px}
.fcol p{line-height:1.6;margin-bottom:10px}
.contact{display:flex;align-items:center;gap:10px;margin-bottom:8px;line-height:1.4}
.contact i{width:26px;height:26px;border-radius:50%;border:1px solid #888;display:flex;align-items:center;justify-content:center;flex:none}
.bottom{height:52px;background:var(--darker);color:#8a8a8a;font-size:11px;text-align:center;line-height:52px}
</style>
</head>
<body>

<header class="hero">
  <div class="hero-photo" role="img" aria-label="Smiling family outdoors in front of a house"></div>
  <div class="hero-shade"></div>
  <div class="topbar">
    <div class="phone"><svg width="14" height="14" viewBox="0 0 24 24"><path fill="#fff" d="M6.6 10.8a15 15 0 006.6 6.6l2.2-2.2c.3-.3.7-.4 1-.2 1.1.4 2.3.6 3.6.6.6 0 1 .4 1 1V20c0 .6-.4 1-1 1A17 17 0 013 4c0-.6.4-1 1-1h3.5c.6 0 1 .4 1 1 0 1.3.2 2.5.6 3.6.1.3 0 .7-.2 1z"/></svg>(02) 5550 1842</div>
    <div class="social"><span style="background:var(--blue)"></span><span style="background:var(--red)"></span><span style="background:var(--yellow)"></span></div>
  </div>
  <div class="brand"><i></i>Brightwell Lending</div>
  <nav class="nav"><a class="active">Home</a><a>About</a><a>Services</a><a>Property Advice</a><a>Contact</a></nav>
  <svg class="arrow l" viewBox="0 0 24 24"><path d="M16 3L7 12l9 9" stroke="#fff" stroke-width="3" fill="none"/></svg>
  <svg class="arrow r" viewBox="0 0 24 24"><path d="M8 3l9 9-9 9" stroke="#fff" stroke-width="3" fill="none"/></svg>
  <div class="hero-copy">
    <h1 class="serif">VIVAMUS ULTRICIES RISUS</h1>
    <p>Donec vel nec augue id amet malesuada. Aenean aliquam tellus dui, ut sodales finibus tincidunt in. Nam vel nec porta risus, nec consequat vel.</p>
    <span class="btn-ghost">BOOK NOW</span>
  </div>
</header>

<section class="rates">
  <h2 class="sec-title serif">NULLAM HENDRERIT</h2>
  <p class="sec-sub">Morbi eget nisi nec id pulvinar augue in ipsum sed lorem porta dui aliquet. Aliquam ut nisl nulla. Nam lectus nibh accumsan a interdum nec.</p>
  <div class="cards">
    <div class="card c1"><h3>SED RUTRUM</h3><div class="rate">3.765%</div><small>VARIABLE RATE</small><hr><div class="rate">2.875%</div><small>FIXED RATE</small><span class="btn">DETAILS</span></div>
    <div class="card c2"><h3>NUNC RUTRUM</h3><div class="rate">3.765%</div><small>VARIABLE RATE</small><hr><div class="rate">2.875%</div><small>FIXED RATE</small><span class="btn">DETAILS</span></div>
    <div class="card c3"><h3>SED RUTRUM</h3><div class="rate">3.765%</div><small>VARIABLE RATE</small><hr><div class="rate">2.875%</div><small>FIXED RATE</small><span class="btn">DETAILS</span></div>
    <div class="card c4"><h3>SED RUTRUM</h3><div class="rate">3.765%</div><small>VARIABLE RATE</small><hr><div class="rate">2.875%</div><small>FIXED RATE</small><span class="btn">DETAILS</span></div>
  </div>
</section>

<section class="feature">
  <div class="feature-photo" role="img" aria-label="Mortgage sign beside a small model house and coins"></div>
  <div class="feature-copy">
    <h2 class="serif">NULLAM HENDRERIT</h2>
    <div class="lead">Duis nec vel sagittis, ornare massa non ipsum sem. Pellentesque quis pharetra dui.</div>
    <p>Quisque id enim dapibus eros porta ligula varius tincidunt sed. Nullam ultrices lacus et augue bibendum tempus. Proin lobortis sed euismod. Pellentesque posuere lectus et arcu, a semper nisi rutrum. Donec accumsan ante at aliquet interdum.</p>
    <span class="btn-ghost">BOOK NOW</span>
  </div>
</section>

<section class="about">
  <h2>About</h2>
  <p class="intro">Sed rutrum ipsum lobortis suscipit volutpat. Ut euismod elit lacus, et accumsan eros commodo vel.</p>
  <p class="body">Pellentesque habitant morbi tristique senectus et netus et malesuada fames ac turpis egestas. Sed fermentum posuere dignissim. Morbi posuere bibendum libero et tristique. Aliquam accumsan nisl nulla hendrerit, in varius massa aliquet.</p>
  <div class="about-photo1" role="img" aria-label="Model house with keys on a desk"></div>
  <div class="about-photo2" role="img" aria-label="Portrait of Marcus Tolven in a suit"></div>
</section>

<section class="testimonials">
  <h2 class="sec-title serif">Testimonials</h2>
  <p class="sec-sub">Nulla eu augue, laoreet in consectetur ut mattis nec diam. Praesent magna ante tempor tincidunt.</p>
  <div class="tcards">
    <div class="tcard"><div class="tphoto" role="img" aria-label="Happy client outdoors" style="background:linear-gradient(135deg,#9fc27a,#5f8a4a)"></div><h4 class="serif">Pellentesque tempus</h4><p>Nam rhoncus lacus tincidunt id Lorem ipsum dolor sit amet, sed tincidunt finibus, leo sed mollis tellus, vel scelerisque orci.</p></div>
    <div class="tcard"><div class="tphoto" role="img" aria-label="Client reading paperwork at home" style="background:linear-gradient(135deg,#efe9df,#b9ac9a)"></div><h4 class="serif">Pellentesque tempus</h4><p>Nam rhoncus lacus tincidunt id Lorem ipsum dolor sit amet, sed tincidunt finibus, leo sed mollis tellus, vel scelerisque orci.</p></div>
    <div class="tcard"><div class="tphoto" role="img" aria-label="Couple carrying moving boxes into a new home" style="background:linear-gradient(135deg,#f2eee8,#c08f6a)"></div><h4 class="serif">Pellentesque tempus</h4><p>Nam rhoncus lacus tincidunt id Lorem ipsum dolor sit amet, sed tincidunt finibus, leo sed mollis tellus, vel scelerisque orci.</p></div>
  </div>
</section>

<section class="consult">
  <div class="consult-photo" role="img" aria-label="Family walking towards a house"></div>
  <div class="consult-shade"></div>
  <h2 class="serif">Free Consultation</h2>
  <div class="form"><div class="field">Your Name</div><div class="field">Your Email</div><div class="field">Your Phone</div></div>
  <div class="submit"><span>SUBMIT</span></div>
</section>

<footer>
  <div class="footer">
    <div class="fcol"><h5>About</h5>Home<br>About<br>Services<br>Property Advice<br>Contact</div>
    <div class="fcol"><h5>Suscipit Eros</h5><p>Morbi accumsan dignissim libero et tristique. Aliquam accumsan id.</p><p>Morbi accumsan dignissim libero et tristique. Aliquam accumsan id.</p></div>
    <div class="fcol"><h5>Contact Us</h5>
      <div class="contact"><i><svg width="12" height="12" viewBox="0 0 24 24"><path fill="#bbb" d="M12 2a7 7 0 00-7 7c0 5 7 13 7 13s7-8 7-13a7 7 0 00-7-7zm0 9.5A2.5 2.5 0 1112 6a2.5 2.5 0 010 5.5z"/></svg></i>48 Larkspur Road, Eastvale</div>
      <div class="contact"><i><svg width="12" height="12" viewBox="0 0 24 24"><path fill="#bbb" d="M6.6 10.8a15 15 0 006.6 6.6l2.2-2.2c.3-.3.7-.4 1-.2 1.1.4 2.3.6 3.6.6.6 0 1 .4 1 1V20c0 .6-.4 1-1 1A17 17 0 013 4c0-.6.4-1 1-1h3.5c.6 0 1 .4 1 1 0 1.3.2 2.5.6 3.6.1.3 0 .7-.2 1z"/></svg></i>(02) 5550 1842</div>
      <div class="contact"><i><svg width="12" height="12" viewBox="0 0 24 24"><path fill="#bbb" d="M2 5h20v14H2zm2 2v.5l8 5 8-5V7z"/></svg></i>hello@brightwell-lending.example</div>
    </div>
  </div>
  <div class="bottom">© 2024 Brightwell Lending. All rights reserved.</div>
</footer>

</body>
</html>
```